Wine label Design

We are looking to develop an elegant contemporary Chilean design; for a new Wine Brand TORVANE to be sold in Chinese Market.
We would like to see designs that are a fine balance between having a traditional design that can offer quality reassurance and being distinctive enough to stand out on crowded shelves. The final design should be easy-to-remember and communicate Quality, Tradition and have a conection with Chile.

Target Market(s)

Urban Chinese between 25 to 40 yo

Requirements
Must have
• Paper label
Information on Front label : Grape (example Cabernet sauvignon) / Vintage (ex 2010) / Wine of Chile
Bottle shape is given (see attached)
Nice to have
• An element of uniqueness, easy to recall the brand
Red and Gold Color are appreciated by the Target
Should not have
• White background
Number 4 is considered death, should not be included on the design

```html
<!DOCTYPE html>
<html lang="en">
<head>
<meta charset="utf-8">
<title>TORVANE Cabernet Sauvignon – Label and Gift Tube</title>
<link rel="stylesheet" href="https://fonts.googleapis.com/css2?family=Cinzel:wght@400&family=Cormorant+Garamond:wght@500&family=Pinyon+Script&family=Lato:wght@400&display=swap">
<style>
  :root {
    --canvas-bg: #ffffff;
    --label-black: #050505;
    --tube-red-deep: #4a0a12;
    --tube-red: #8a1626;
    --tube-red-light: #9e1f30;
    --ornament-red: #b0283a;
    --ornament-red-dark: #6e0f1c;
    --ornament-grey: #2a2a2a;
    --gold: #d9a22b;
    --gold-deep: #b07a16;
    --name-white: #f4f1ec;
    --varietal-red: #9c2730;
    --caption-grey: #9a9a9a;
  }
  * { margin: 0; padding: 0; box-sizing: border-box; }
  html, body { width: 1200px; height: 848px; overflow: hidden; background: var(--canvas-bg); }
  .canvas { position: relative; width: 1200px; height: 848px; }

  /* Gift tube wrap, shown flat */
  .tube-wrap {
    position: absolute; left: 317px; top: 30px; width: 200px; height: 760px;
    background: linear-gradient(90deg, var(--tube-red-deep) 0%, var(--tube-red) 30%, var(--tube-red-light) 55%, var(--tube-red) 80%, var(--tube-red-deep) 100%);
  }
  .tube-wrap .ornament-field {
    position: absolute; left: 8px; top: 120px; width: 184px; height: 440px;
    border-radius: 50%;
    background: radial-gradient(ellipse at center, rgba(110,15,28,0.15) 0%, rgba(176,40,58,0.75) 45%, rgba(110,15,28,0.55) 68%, rgba(110,15,28,0) 100%);
  }
  .tube-wrap .crest {
    position: absolute; left: 62px; top: 262px; width: 76px; height: 40px;
    border-radius: 38px 38px 6px 6px;
    background: linear-gradient(180deg, var(--gold) 0%, var(--gold-deep) 100%);
  }
  .tube-wrap .brand-name {
    position: absolute; left: 0; top: 312px; width: 100%; text-align: center;
    font-family: "Cinzel", serif; font-weight: 400; font-size: 29px; letter-spacing: 1px;
    color: var(--name-white);
  }

  /* Front label */
  .front-label {
    position: absolute; left: 728px; top: 184px; width: 284px; height: 373px;
    background: var(--label-black);
  }
  .front-label .vintage {
    position: absolute; top: 26px; width: 100%; text-align: center;
    font-family: "Cormorant Garamond", serif; font-size: 18px; color: var(--gold);
    font-variant-numeric: lining-nums;
  }
  .front-label .ornament-field {
    position: absolute; left: 20px; top: 48px; width: 244px; height: 258px;
    border-radius: 50%;
    background: radial-gradient(ellipse at center, rgba(42,42,42,0.2) 0%, rgba(58,58,58,0.85) 40%, rgba(42,42,42,0.6) 65%, rgba(5,5,5,0) 100%);
  }
  .front-label .crest {
    position: absolute; left: 108px; top: 120px; width: 68px; height: 30px;
    border-radius: 30px 30px 5px 5px;
    background: linear-gradient(180deg, var(--gold) 0%, var(--gold-deep) 100%);
  }
  .front-label .brand-name {
    position: absolute; top: 152px; width: 100%; text-align: center;
    font-family: "Cinzel", serif; font-weight: 400; font-size: 29px; letter-spacing: 1px;
    color: var(--name-white);
  }
  .front-label .varietal {
    position: absolute; top: 296px; width: 100%; text-align: center;
    font-family: "Pinyon Script", cursive; font-size: 20px; color: var(--varietal-red);
  }
  .front-label .origin {
    position: absolute; top: 343px; width: 100%; text-align: center;
    font-family: "Lato", sans-serif; font-size: 10px; letter-spacing: 2.5px; color: var(--caption-grey);
  }
</style>
</head>
<body>
<main class="canvas">
  <section class="tube-wrap" aria-label="Gift tube wrap">
    <div class="ornament-field" role="img" aria-label="Symmetrical red floral scroll ornament"></div>
    <div class="crest" role="img" aria-label="Small gold floral crest ornament"></div>
    <h2 class="brand-name">TORVANE</h2>
  </section>

  <section class="front-label" aria-label="Front label">
    <p class="vintage">2010</p>
    <div class="ornament-field" role="img" aria-label="Dark grey floral scroll ornament with small red berries"></div>
    <div class="crest" role="img" aria-label="Small gold floral crest ornament"></div>
    <h1 class="brand-name">TORVANE</h1>
    <p class="varietal">Cabernet Sauvignon</p>
    <p class="origin">WINE OF CHILE</p>
  </section>
</main>
</body>
</html>
```